A layout of a webpage for oil trade platform

I would like to have a desgin of one page webpage (with section scrollling dowin) that woulf present the new product i.e. oil trade platform for wholesale buyers and sellers.
Layout should consist of the sections similar to the given at: https://strona.trawomirek.pl/modul-planowania-spotkan
However oil industy require more colors and more photo stories than here for doctor.
I. I woul imagine at first below menu a slider with brueg information about the product and its advantages with "more" button next to the prict screen of our platform on different displays (PC and mobile).
II. Bellow the slider I would imagine icons correspoing to the advantages of that plaftorm:
1. Purchase/sale process automation 24/7
2. Access to the best deals
3. Electronic offerings and orderings
4. Transaction status monitoring
5. Data and transaction security
II A) (optional):
In near future we would like to prepare a short video presenation. Hence please prepare a place to display that element here.
At the moment alternatvily please prepare a How it works section that would explan the platform operating process
III. Next secion is about benefits for Oil Purchaser
It can be done either by icons of by text and corresponding grahip for while section.
Benefits:
- Access to cheaper oil
- Convenience of online orders
- Possibility to compare prices on the market
- Transaction history
- Order status monitoring
- Seccurity and transparency of purchase
IV. Next seciont is about benefits for Oil Seller
Benefits:
- New sale channel
- Attracting new clients
- More oil sold
- Transaction security
- Possibility to integrate with distribution infrastructure and logistits for more efficient automation.
V. Contact form
VI. Footer
I would need a layout that that will correspond to the very dynamic logo but I would expect also a clean form, smoth and modern. It has to be proffessional layout with more corporate character.
It can use a paralax features if needed.
Attachments:
- logo design
- platfrom print screen
Industry/Entity Type
Oil And Gas
Number of Pages Required
1 page

```html
<!DOCTYPE html>
<html lang="en">
<head>
<meta charset="utf-8">
<title>Crudeline — Oil Trade Platform</title>
<link rel="stylesheet" href="https://fonts.googleapis.com/css2?family=Roboto:wght@300;400;500;700&display=swap">
<style>
:root{
  --navy:#0f2350;
  --navy-deep:#0a1a3e;
  --navy-sea:#1b3363;
  --orange:#f68b2c;
  --ink:#1d2433;
  --text:#555b66;
  --muted:#8a8f99;
  --line:#e3e5ea;
  --panel:#f5f5f6;
  --white:#ffffff;
  --footer:#2b2420;
  --footer-bar:#1c1816;
}
*{box-sizing:border-box;margin:0;padding:0}
html,body{width:1200px;height:2289px;overflow:hidden}
body{font-family:'Roboto',sans-serif;color:var(--text);background:var(--white);position:relative}
ul{list-style:none}

/* header */
.site-header{position:absolute;top:0;left:0;width:1200px;height:78px;background:#f8f8f8;display:flex;align-items:center;justify-content:space-between;padding:0 122px 0 116px}
.brand{display:flex;align-items:center;gap:10px;font-weight:700;font-size:20px;color:var(--navy)}
.brand-dot{width:30px;height:30px;border-radius:50%;background:var(--orange)}
.main-nav{display:flex;font-size:15px;color:#555}
.main-nav a{padding:0 16px;color:inherit;text-decoration:none;border-left:1px solid #ccc;line-height:14px}
.main-nav a:first-child{border-left:none;color:var(--ink);font-weight:500}
.main-nav a:last-child{padding-right:0}

/* hero */
.hero{position:absolute;top:78px;left:0;width:1200px;height:515px;background:radial-gradient(ellipse at 60% 40%,#1d3468 0%,var(--navy) 55%,var(--navy-deep) 100%);text-align:center;color:var(--white)}
.hero-eyebrow{position:absolute;top:130px;width:100%;font-weight:300;font-size:28px;letter-spacing:1px}
.hero-title{position:absolute;top:158px;width:100%;font-weight:400;font-size:44px;letter-spacing:.5px}
.hero-title span{font-weight:300}
.hero-text{position:absolute;top:216px;left:238px;width:724px;font-size:15px;line-height:24px;color:#d4daea;font-weight:300}
.hero-btn{position:absolute;top:325px;left:518px;width:162px;height:44px;border:1px solid #fff;font-size:16px;line-height:42px;letter-spacing:.5px}
.hero-dots{position:absolute;top:387px;left:582px;display:flex;gap:5px}
.hero-dots i{width:8px;height:8px;border-radius:50%;background:#fff}
.hero-dots i:first-child{background:var(--orange)}
.scroll-mouse{position:absolute;top:429px;left:583px;width:34px;height:60px;border:2px solid #fff;border-radius:17px}
.scroll-mouse::after{content:"";position:absolute;top:11px;left:14px;width:2px;height:8px;background:#fff}

/* features */
.features{position:absolute;top:593px;left:0;width:1200px;height:120px;display:flex;background:var(--white)}
.feature{flex:1;border-right:1px solid var(--line);display:flex;flex-direction:column;align-items:center;padding-top:18px;text-align:center;font-size:12px;line-height:15px;color:var(--muted)}
.feature:last-child{border-right:none}
.feature svg{width:40px;height:40px;margin-bottom:8px;stroke:var(--orange);fill:none;stroke-width:1.6}
.feature.is-active{background:var(--orange);color:var(--white)}
.feature.is-active svg{stroke:#fff}

/* purchaser */
.purchaser{position:absolute;top:713px;left:0;width:1200px;height:525px;background:var(--panel)}
.purchaser-photo{position:absolute;top:0;left:0;width:600px;height:525px;background:linear-gradient(135deg,#e9eef3 0%,#b9c6d3 40%,#4a5566 75%,#2a2f3a 100%)}
.benefits-title{font-size:26px;font-weight:300;color:var(--ink)}
.benefits-title strong{font-weight:500}
.purchaser .benefits-title{position:absolute;top:78px;left:674px}
.purchaser-list{position:absolute;top:131px;left:656px;width:434px}
.purchaser-list li{height:51px;display:flex;align-items:center;padding-left:22px;font-size:15px;color:var(--text)}
.purchaser-list li.is-highlight{background:var(--white);box-shadow:0 2px 8px rgba(0,0,0,.07)}
.purchaser-list svg{width:28px;height:28px;margin-right:20px;stroke:#333;fill:none;stroke-width:1.6}
.video-btn{position:absolute;top:1216px;left:989px;width:44px;height:44px;border-radius:50%;background:var(--orange);z-index:2;display:flex;align-items:center;justify-content:center}
.video-btn svg{width:20px;height:16px;stroke:#fff;fill:none;stroke-width:1.6}

/* seller */
.seller{position:absolute;top:1238px;left:0;width:1200px;height:517px;background:linear-gradient(180deg,#233d70 0%,var(--navy-sea) 45%,#152b58 100%);color:var(--white)}
.seller .benefits-title{position:absolute;top:112px;left:180px;color:var(--white)}
.seller-list{position:absolute;top:164px;left:180px;width:360px}
.seller-list li{min-height:53px;display:flex;align-items:flex-start;font-size:15px;line-height:19px;color:#e5e9f2}
.seller-list svg{flex:none;width:32px;height:32px;margin:-6px 22px 0 0;stroke:#fff;fill:none;stroke-width:1.5}

/* contact */
.contact{position:absolute;top:1755px;left:0;width:1200px;height:290px;background:#f8f8f8;text-align:center}
.contact-title{position:absolute;top:40px;width:100%;font-size:26px;font-weight:300;color:var(--ink)}
.contact-title strong{font-weight:500}
.contact-text{position:absolute;top:87px;left:160px;width:880px;font-size:12px;line-height:20px;color:var(--muted)}
.contact-form{position:absolute;top:151px;left:269px;width:662px;height:76px}
.field{position:absolute;background:var(--white);border:1px solid #ececec;font-size:12px;color:var(--muted);text-align:left;display:flex;align-items:center;padding-left:10px}
.field svg{width:12px;height:12px;margin-right:8px;fill:#c5c8ce}
.field-name{top:0;left:0;width:268px;height:37px}
.field-email{top:39px;left:0;width:268px;height:37px}
.field-message{top:0;left:274px;width:270px;height:76px;align-items:flex-start;padding-top:10px}
.send-btn{position:absolute;top:0;left:550px;width:112px;height:76px;background:var(--orange);color:#fff;font-size:26px;line-height:76px;text-align:center}

/* footer */
.site-footer{position:absolute;top:2045px;left:0;width:1200px;height:200px;background:linear-gradient(180deg,#3a302a 0%,var(--footer) 100%);border-top:3px solid var(--orange);color:#e8e2dc;font-size:11px}
.footer-col{position:absolute;top:26px}
.footer-col h3{font-size:14px;line-height:16px;font-weight:500;color:#fff;margin-bottom:12px}
.footer-col li{line-height:20.5px}
.col-life{left:110px}
.col-life-extra{left:249px;top:54px}
.col-careers{left:420px}
.col-events{left:691px}
.col-contact{left:945px}
.contact-row{display:flex;gap:8px;line-height:14px;margin-bottom:10px}
.contact-row svg{flex:none;width:11px;height:11px;fill:#cfc7bf;margin-top:2px}
.contact-row.is-phone{font-size:14px}
.footer-bar{position:absolute;top:2245px;left:0;width:1200px;height:44px;background:var(--footer-bar);display:flex;align-items:center;justify-content:space-between;padding:0 110px;font-size:10px;color:#bdb5ad}
.follow{display:flex;align-items:center;gap:4px;font-size:13px;font-style:italic;color:#fff}
.follow span{margin-right:8px}
.social-box{width:22px;height:22px;background:#6c7a8e}
</style>
</head>
<body>

<header class="site-header">
  <div class="brand"><span class="brand-dot"></span>Crudeline</div>
  <nav class="main-nav">
    <a>Home</a><a>Company</a><a>Energy News</a><a>Projects</a><a>Contact Us</a>
  </nav>
</header>

<section class="hero" role="img" aria-label="Dark blue backdrop of an oil and gas pipeline facility">
  <div class="hero-eyebrow">TRANSPORTING</div>
  <h1 class="hero-title">OIL <span>&amp;</span> NATURAL GAS</h1>
  <p class="hero-text">Advances in exploration and production have helped to locate and recover a supply of oil and natural gas from major reserves across the globe. At the same time, demand for petroleum-based products has grown in every corner of the world.</p>
  <div class="hero-btn">LEARN MORE</div>
  <div class="hero-dots"><i></i><i></i><i></i></div>
  <div class="scroll-mouse"></div>
</section>

<section class="features">
  <div class="feature">
    <svg viewBox="0 0 40 40"><circle cx="20" cy="20" r="11"/><path d="M8 12a15 15 0 0 1 26 0M32 28a15 15 0 0 1-26 0M34 8v4h-4M6 32v-4h4M20 14v12M17 17h5a2 2 0 0 1 0 4h-4a2 2 0 0 0 0 4h5"/></svg>
    Purchase/sale process<br>automation 24/7
  </div>
  <div class="feature">
    <svg viewBox="0 0 40 40"><path d="M4 18l8-8 6 4 6-4 12 8M4 18l10 10 4-3 4 4 4-3 10-10M14 16l6 6"/></svg>
    Access to<br>the best deals
  </div>
  <div class="feature is-active">
    <svg viewBox="0 0 40 40"><path d="M20 4l4 4h6v6l4 4-4 4v6h-6l-4 4-4-4h-6v-6l-4-4 4-4V8h6z"/><path d="M15 25l10-10"/><circle cx="16" cy="16" r="1.5"/><circle cx="24" cy="24" r="1.5"/></svg>
    Electronic offerings<br>and orderings
  </div>
  <div class="feature">
    <svg viewBox="0 0 40 40"><rect x="5" y="7" width="30" height="20"/><path d="M15 33h10M20 27v6M20 12v6l3 3"/></svg>
    Transaction status<br>monitoring
  </div>
  <div class="feature">
    <svg viewBox="0 0 40 40"><ellipse cx="20" cy="9" rx="11" ry="4"/><path d="M9 9v22c0 2 5 4 11 4s11-2 11-4V9M9 17c0 2 5 4 11 4s11-2 11-4M9 25c0 2 5 4 11 4s11-2 11-4"/></svg>
    Data and transaction<br>security
  </div>
</section>

<section class="purchaser">
  <div class="purchaser-photo" role="img" aria-label="Photo of two businessmen working together at a laptop in a bright office"></div>
  <h2 class="benefits-title">Oil Purchaser <strong>Benefits</strong></h2>
  <ul class="purchaser-list">
    <li><svg viewBox="0 0 28 28"><circle cx="9" cy="9" r="5"/><path d="M12 12l12 12M19 19l3-3M22 22l2-2"/></svg>Access to cheaper oil</li>
    <li><svg viewBox="0 0 28 28"><path d="M3 5h4l3 13h12l3-9H9"/><circle cx="11" cy="23" r="1.8"/><circle cx="21" cy="23" r="1.8"/></svg>Convenience of online orders</li>
    <li class="is-highlight"><svg viewBox="0 0 28 28"><path d="M3 24h22M6 24v-6M10 24v-9M14 24v-6M18 24v-11M22 24V8"/></svg>Possibility to compare prices on the market</li>
    <li><svg viewBox="0 0 28 28"><path d="M5 14a9 9 0 1 0 3-6.7M5 5v4h4M14 9v5l3 3"/></svg>Transaction history</li>
    <li><svg viewBox="0 0 28 28"><rect x="3" y="6" width="15" height="13" rx="2"/><path d="M18 10h4l3 4v5h-7"/><circle cx="8" cy="21" r="2"/><circle cx="21" cy="21" r="2"/><path d="M7 12l3 3 5-5"/></svg>Order status monitoring</li>
    <li><svg viewBox="0 0 28 28" style="fill:#333;stroke:none"><circle cx="5" cy="5" r="2"/><circle cx="11" cy="5" r="2"/><circle cx="17" cy="5" r="2"/><circle cx="5" cy="11" r="2"/><circle cx="11" cy="11" r="2"/><circle cx="5" cy="17" r="2"/><circle cx="11" cy="17" r="2"/><circle cx="17" cy="17" r="2"/><circle cx="23" cy="17" r="2"/><circle cx="5" cy="23" r="2"/><circle cx="11" cy="23" r="2"/><circle cx="17" cy="23" r="2"/></svg>Seccurity and transparency of purchase</li>
  </ul>
</section>

<div class="video-btn"><svg viewBox="0 0 20 16"><rect x="1" y="1" width="18" height="14" rx="2"/><path d="M8 5l5 3-5 3z"/></svg></div>

<section class="seller" role="img" aria-label="Blue-toned sea scene with an offshore oil platform and a supply ship">
  <h2 class="benefits-title">Oil Seller <strong>Benefits</strong></h2>
  <ul class="seller-list">
    <li><svg viewBox="0 0 32 32"><path d="M4 16L16 4h12v12L16 28z"/><circle cx="22" cy="10" r="2"/><path d="M12 18l6-6"/></svg>New sale channel</li>
    <li><svg viewBox="0 0 32 32"><circle cx="16" cy="16" r="3"/><circle cx="16" cy="5" r="2"/><circle cx="16" cy="27" r="2"/><circle cx="5" cy="16" r="2"/><circle cx="27" cy="16" r="2"/><circle cx="8" cy="8" r="2"/><circle cx="24" cy="8" r="2"/><circle cx="8" cy="24" r="2"/><circle cx="24" cy="24" r="2"/></svg>Attracting new clients</li>
    <li><svg viewBox="0 0 32 32"><path d="M4 4v24h24M8 24l6-8 5 4 8-12M23 8h4v4"/></svg>More oil sold</li>
    <li><svg viewBox="0 0 32 32"><rect x="4" y="6" width="24" height="16"/><path d="M2 26h28"/><circle cx="16" cy="13" r="4"/><path d="M14 13l1.5 1.5L18 12"/></svg>Transaction security</li>
    <li><svg viewBox="0 0 32 32"><path d="M3 28h26M6 28V12h4v16M14 28V8h4v20M22 28V14h4v16M8 12V4M16 8V2M24 14V8M4 4h8M12 2h8M20 8h8"/></svg>Possibility to integrate with distribution infrastructure and logistits for more efficient automation</li>
  </ul>
</section>

<section class="contact">
  <h2 class="contact-title">Contact <strong>Us</strong></h2>
  <p class="contact-text">Reach our trading desk with any question about listing, buying or delivery. Share a few details, our team will reply within one business day with the next steps. We keep every enquiry private and use it only to answer you.</p>
  <div class="contact-form">
    <div class="field field-name"><svg viewBox="0 0 12 12"><circle cx="6" cy="3.5" r="3"/><path d="M0 12a6 5 0 0 1 12 0z"/></svg>Name</div>
    <div class="field field-email"><svg viewBox="0 0 12 12"><rect x="0" y="2" width="12" height="8" rx="1"/></svg>Email</div>
    <div class="field field-message">Message</div>
    <div class="send-btn">Send</div>
  </div>
</section>

<footer class="site-footer">
  <div class="footer-col col-life">
    <h3>Life in Oil &amp; Gas</h3>
    <ul><li>Oil and Gas Journey</li><li>Oil and Gas Guide</li><li>Life Onshore</li><li>Life Offshore</li><li>Training</li><li>Safety</li></ul>
  </div>
  <div class="footer-col col-life-extra">
    <ul><li>Case Studies</li><li>Energy Skills Library</li></ul>
  </div>
  <div class="footer-col col-careers">
    <h3>Careers</h3>
    <ul><li>Oil &amp; Gas Industry Roles</li><li>Career Planner</li><li>Find a job</li><li>Oil and Gas Company Careers Websites</li><li>Oil and Gas Technica</li><li>Skills Matrix</li></ul>
  </div>
  <div class="footer-col col-events">
    <h3>Events</h3>
    <ul><li>Energise Your Future</li><li>Industry Awareness Events</li><li>MyEnergyCareer App</li><li>Resources</li><li>Pipeline of Information Week</li><li>Platform of Opportunity Week</li></ul>
  </div>
  <div class="footer-col col-contact">
    <h3>Contact</h3>
    <div class="contact-row"><svg viewBox="0 0 12 12"><path d="M6 0a4 4 0 0 1 4 4c0 3-4 8-4 8S2 7 2 4a4 4 0 0 1 4-4z"/></svg><div>Crudeline<br>4410 W. Harbor Ave.<br>STE 12 - 300<br>Tulsa, OK 74107</div></div>
    <div class="contact-row is-phone"><svg viewBox="0 0 12 12"><rect x="0" y="2" width="12" height="8" rx="1"/></svg>(800) 555-0142</div>
    <div class="contact-row"><svg viewBox="0 0 12 12"><rect x="0" y="2" width="12" height="8" rx="1"/></svg>sales@crudeline.example</div>
  </div>
</footer>

<div class="footer-bar">
  <span>© 2017 Crudeline.  All Rights Reserved.</span>
  <div class="follow"><span>Follow Us On</span><i class="social-box"></i><i class="social-box"></i><i class="social-box"></i><i class="social-box"></i></div>
</div>

</body>
</html>
```